Letterhead for new real estate company in South Africa named Tallowick

A letterhead with the directors and company details to be editable as these changes often

Target Market(s)

In line with our logo brief and our newly designed logo and corporate fee

Industry/Entity Type

Real Estate

Requirements
Must have
• Details as per the sample letterhead provided.

```html
<!DOCTYPE html>
<html lang="en">
<head>
<meta charset="utf-8">
<title>Tallowick Letterhead</title>
<link href="https://fonts.googleapis.com/css2?family=Lato:wght@400;700&family=Cabin+Condensed:wght@400&display=swap" rel="stylesheet">
<style>
  :root {
    --brand-green: #2db36f;
    --brand-earth: #6e665b;
    --ink: #4f4f4f;
    --ink-soft: #555555;
    --paper: #ffffff;
    --backdrop: #d6d6d6;
  }
  * { margin: 0; padding: 0; box-sizing: border-box; }
  html, body {
    width: 1056px; height: 1200px; overflow: hidden;
    background: var(--backdrop);
  }
  .letterhead {
    position: absolute; left: 104px; top: 0;
    width: 848px; height: 1200px;
    background: var(--paper);
    font-family: "Lato", sans-serif;
    color: var(--ink);
  }
  .brand {
    position: absolute; left: 78px; top: 92px;
    display: flex; align-items: center; gap: 10px;
  }
  .brand-dot {
    width: 26px; height: 26px; border-radius: 50%;
    background: var(--brand-green);
  }
  .brand-name {
    font-family: "Lato", sans-serif; font-weight: 400;
    font-size: 29px; letter-spacing: 0.5px;
    color: var(--brand-green); text-transform: uppercase;
  }
  .directors {
    position: absolute; right: 252px; top: 86px;
    text-align: right;
  }
  .directors-title {
    font-weight: 700; font-size: 14.5px; color: var(--brand-green);
    margin-bottom: 6px;
  }
  .directors-list { list-style: none; font-size: 12px; line-height: 14.5px; color: var(--ink-soft); }
  .header-divider {
    position: absolute; left: 614px; top: 73px;
    width: 1px; height: 74px; background: var(--brand-green);
  }
  .contact {
    position: absolute; left: 631px; top: 68px;
    font-size: 11.5px; line-height: 14.5px; color: var(--ink-soft);
  }
  .contact-address { font-style: normal; margin-bottom: 6px; }
  .contact-line { display: flex; align-items: center; gap: 10px; height: 16.5px; }
  .contact-line svg { width: 12px; height: 12px; flex: none; }
  .letter-body {
    position: absolute; left: 78px; top: 395px; width: 689px;
    font-family: "Cabin Condensed", sans-serif;
    font-size: 20px; line-height: 29.5px; color: var(--ink);
  }
  .letter-body p { text-align: justify; margin-bottom: 29.5px; }
  .letter-body .salutation { margin-bottom: 25.5px; }
  .sign-off {
    position: absolute; left: 78px; top: 987px;
    font-family: "Cabin Condensed", sans-serif;
    font-size: 20px; color: var(--ink);
  }
  .signature {
    position: absolute; left: 74px; top: 1024px;
    width: 68px; height: 40px;
    background: linear-gradient(90deg, rgba(45,179,111,0.18), rgba(45,179,111,0.35));
    border-radius: 4px;
  }
  .footer-rule {
    position: absolute; left: 78px; top: 1156px;
    width: 351px; height: 1px; background: var(--brand-green);
  }
  .footer-note {
    position: absolute; right: 81px; top: 1147px;
    font-size: 13.5px; color: var(--ink-soft);
  }
  .footer-band { position: absolute; left: 0; bottom: 0; width: 848px; height: 18px; }
</style>
</head>
<body>
  <main class="letterhead">
    <header>
      <div class="brand">
        <span class="brand-dot"></span>
        <span class="brand-name">Tallowick</span>
      </div>

      <section class="directors">
        <h2 class="directors-title">Directors:</h2>
        <ul class="directors-list">
          <li>L Venter</li>
          <li>RJ Dlamini -Hart</li>
        </ul>
      </section>

      <div class="header-divider"></div>

      <section class="contact">
        <address class="contact-address">
          Shop GF12B, Acacia Village,<br>
          Corner Kestrel Avenue &amp;<br>
          Marula Lane Acacia, SA
        </address>
        <div class="contact-line">
          <svg viewBox="0 0 24 24" aria-hidden="true"><path fill="var(--brand-green)" d="M6.6 10.8c1.4 2.8 3.8 5.1 6.6 6.6l2.2-2.2c.3-.3.7-.4 1-.2 1.1.4 2.3.6 3.6.6.6 0 1 .4 1 1V20c0 .6-.4 1-1 1C10.6 21 3 13.4 3 4c0-.6.4-1 1-1h3.5c.6 0 1 .4 1 1 0 1.3.2 2.5.6 3.6.1.3 0 .7-.2 1z"/></svg>
          <span>010 555 0148</span>
        </div>
        <div class="contact-line">
          <svg viewBox="0 0 24 24" aria-hidden="true"><circle cx="12" cy="12" r="9.5" fill="none" stroke="var(--brand-green)" stroke-width="2"/><ellipse cx="12" cy="12" rx="4" ry="9.5" fill="none" stroke="var(--brand-green)" stroke-width="1.6"/><path d="M3 12h18" stroke="var(--brand-green)" stroke-width="1.6"/></svg>
          <span>www.tallowickhomes.co.za</span>
        </div>
      </section>
    </header>

    <article class="letter-body">
      <p class="salutation">Dear Sir/Mam,</p>
      <p>Contrary to popular belief, Lorem Ipsum is not simply random text. It has roots in a piece of classical Latin literature from 45 BC, making it over 2000 years old. Henry Waverley, a Latin professor at Ashbury-Lane College in Virginia, looked up one of the more obscure Latin words, consectetur.</p>
      <p>Lorem Ipsum comes from sections 1.10.32 and 1.10.33 of "de Finibus Bonorum et Malorum" (The Extremes of Good and Evil) by Varronius, written in 45 BC. This book is a treatise on the theory of ethics, very popular during the Renaissance. The first line of Lorem Ipsum.</p>
      <p>The standard chunk of Lorem Ipsum used since the 1500s is reproduced below for those interested. Sections 1.10.32 and 1.10.33 from "de Finibus Bonorum et Malorum" by Varronius are also reproduced in their exact original.</p>
      <p>The standard chunk of Lorem Ipsum used since the 1500s is reproduced below for those interested.</p>
    </article>

    <p class="sign-off">Best Regards</p>
    <div class="signature" role="img" aria-label="Handwritten signature of the sender"></div>

    <footer>
      <div class="footer-rule"></div>
      <p class="footer-note">Each franchise is independently owned and operated</p>
      <svg class="footer-band" viewBox="0 0 848 18" preserveAspectRatio="none" aria-hidden="true">
        <polygon points="0,0 435,0 425,18 0,18" fill="var(--brand-green)"/>
        <polygon points="444,0 848,0 848,18 434,18" fill="var(--brand-earth)"/>
      </svg>
    </footer>
  </main>
</body>
</html>
```